依頼詳細
お客様と話をする際、代理店や営業マンがお客様にお見せして、瞬時にポイントがわかり、詳細まで見たくなる仕上がりにしたいと考えています。
記載項目
文字、文言は添付ファイルにでています。
記載したい文字や協調したい文言は、文字の大きさで表現していますので、参考
にしてください。
表面
配置や色使いはお任せ致します。ポイントが目に飛び込んでくる様な仕上げに
してください。
裏面
事例が4例でてます。ポイントは赤字にしてありますが、元の配置や文字ポイン
ト・色は無視
して頂いて結構です。ポイントがわかりやすい仕上がりでお願い致します。
グラフについても同様で、意味が同じであればどんな色でもOKです。

サイズ
A4
ページ数
両面
希望イメージ
シンプル 複雑
単色 カラフル
暗い 明るい
日常 高級
遊び心 厳粛
未来的 伝統的
女性的 男性的
希望する色
水色系、グレー系
納品ファイル
• イラストレーター形式 (.ai)
補足説明
構成やデザインについての変更は、ありませんが文字(数値)などの変更をお願いする事がありますので、その節には対応の程お願い致します。
ロゴは、aiファイルに貼ってあります。
■ 選んだ理由

本当に悩みましたが
今回の利用目的を考慮した結果です。

■ 提案者全員のお礼・コメント

本当に、迷いました。
また機会がございましたら、是非ご応募いただきます様お願い致します。
皆さま方の今後の活躍を期待しております。

```html
<!DOCTYPE html>
<html lang="ja">
<head>
<meta charset="utf-8">
<title>電気代削減の新低案</title>
<link rel="stylesheet" href="https://fonts.googleapis.com/css2?family=Noto+Sans+JP:wght@400;700;900&display=swap">
<style>
  :root {
    --navy: #1d2d4f;
    --ink: #161616;
    --red: #d7191e;
    --red-light: #ff4a4a;
    --sky: #a9d3ee;
    --sky-pale: #e3f1fa;
    --blue: #2f7fc1;
    --white: #ffffff;
  }
  html, body { margin: 0; padding: 0; overflow: hidden; }
  body { width: 846px; height: 1200px; font-family: "Noto Sans JP", sans-serif; }
  p, h1 { margin: 0; }
  .flyer {
    position: relative; width: 846px; height: 1200px; overflow: hidden;
    background: linear-gradient(180deg, var(--sky-pale) 0%, #ffffff 30%, #eef6fb 46%, var(--sky) 100%);
  }
  .top-band {
    position: absolute; left: 0; top: 0; width: 846px; height: 44px;
    background: var(--navy); color: var(--white);
    font-weight: 700; font-size: 22px; line-height: 44px; text-align: center; letter-spacing: 1px;
  }
  .top-band em { font-style: normal; color: var(--red-light); }
  .lead-band {
    position: absolute; left: 0; top: 66px; width: 846px; height: 70px;
    background: linear-gradient(90deg, rgba(169,211,238,0) 0%, rgba(169,211,238,.85) 20%, rgba(169,211,238,.85) 80%, rgba(169,211,238,0) 100%);
  }
  .lead {
    position: absolute; left: 0; top: 76px; width: 846px; text-align: center;
    font-weight: 900; font-size: 36px; color: var(--navy); letter-spacing: 2px;
  }
  .headline {
    position: absolute; left: 0; top: 150px; width: 846px; text-align: center;
    font-weight: 900; font-size: 112px; line-height: 1.1; color: var(--ink); letter-spacing: 4px;
  }
  .proposal {
    position: absolute; left: 90px; top: 300px; width: 640px; height: 240px;
    display: flex; align-items: center; justify-content: center; gap: 14px;
  }
  .proposal .big { font-weight: 900; font-size: 190px; color: var(--ink); line-height: 1; }
  .low-arrow { position: relative; width: 210px; height: 240px; }
  .low-arrow svg { position: absolute; inset: 0; }
  .low-arrow span {
    position: absolute; left: 0; top: 18px; width: 210px; text-align: center;
    font-weight: 900; font-size: 150px; line-height: 1; color: var(--white);
  }
  .exclaim { position: absolute; left: 720px; top: 190px; }
  .feature-area {
    position: absolute; left: 0; top: 560px; width: 846px; height: 420px;
    background: linear-gradient(180deg, #5f8fb8 0%, #3f6f9d 55%, #6aa3cf 100%);
  }
  .band { position: absolute; left: 150px; width: 560px; height: 108px; background: rgba(29,45,79,.78); }
  .band.light { background: rgba(255,255,255,.92); }
  .line {
    position: absolute; left: 170px; font-weight: 900; font-size: 37px; line-height: 1.3;
    color: var(--white); letter-spacing: 1px;
  }
  .line.red { color: var(--red); }
  .badge-circle {
    position: absolute; width: 110px; height: 110px; border-radius: 50%;
    background: var(--red); color: var(--white); border: 4px solid var(--white);
    display: flex; align-items: center; justify-content: center; text-align: center;
    font-weight: 900; font-size: 22px; line-height: 1.2; box-sizing: border-box;
  }
  .badge-circle.small { width: 92px; height: 92px; font-size: 26px; }
  .cost-tag {
    position: absolute; width: 70px; height: 64px; background: var(--white);
    border: 3px solid var(--ink); box-sizing: border-box; text-align: center;
  }
  .cost-tag small { display: block; font-size: 10px; font-weight: 700; color: var(--red); line-height: 16px; }
  .cost-tag b { display: block; font-size: 32px; font-weight: 900; color: var(--ink); line-height: 38px; }
  .note {
    position: absolute; left: 170px; top: 835px; width: 560px;
    font-size: 12.5px; line-height: 1.7; color: var(--white);
  }
  .about {
    position: absolute; left: 48px; top: 996px; width: 750px;
    font-weight: 700; font-size: 20px; line-height: 1.6; color: var(--navy);
  }
  .about strong { color: var(--red); font-weight: 700; }
  .about em { font-style: normal; color: var(--blue); }
  .brand {
    position: absolute; left: 0; top: 1128px; width: 846px;
    display: flex; align-items: center; justify-content: center; gap: 12px;
  }
  .brand i { width: 34px; height: 34px; border-radius: 50%; background: var(--red); display: block; }
  .brand span { font-weight: 900; font-size: 36px; color: var(--navy); line-height: 1; }
  .brand-sub { position: absolute; left: 0; top: 1172px; width: 846px; text-align: center; font-size: 13px; font-weight: 900; color: var(--navy); }
</style>
</head>
<body>
<main class="flyer">
  <header class="top-band">電力供給を通して省エネ・省電力・省CO₂の<em>新しいご提案!</em></header>

  <div class="lead-band"></div>
  <p class="lead">省エネ診断ができる新電力会社からの</p>
  <h1 class="headline">電気代削減の</h1>

  <div class="proposal">
    <span class="big">新</span>
    <div class="low-arrow">
      <svg width="210" height="240" viewBox="0 0 210 240">
        <polygon points="8,0 202,0 202,165 105,238 8,165" fill="#161616"/>
      </svg>
      <span>低</span>
    </div>
    <span class="big">案</span>
  </div>

  <svg class="exclaim" width="90" height="200" viewBox="0 0 90 200">
    <polygon points="30,0 52,0 24,150 8,150" fill="#d7191e"/>
    <polygon points="70,0 90,0 62,150 46,150" fill="#d7191e"/>
    <circle cx="14" cy="182" r="10" fill="#d7191e"/>
    <circle cx="52" cy="182" r="10" fill="#d7191e"/>
  </svg>

  <section class="feature-area" role="img" aria-label="オフィスで打ち合わせをするビジネスパーソンの写真"></section>

  <div class="band" style="top:590px"></div>
  <p class="line" style="top:592px">LED交換で消費電力削減</p>
  <p class="line" style="top:643px">新電力導入で電気代削減</p>
  <div class="badge-circle" style="left:50px;top:585px">工事費も<br>安い!</div>
  <div class="cost-tag" style="left:718px;top:610px"><small>COST DOWN</small><b>低</b></div>

  <div class="band light" style="top:712px"></div>
  <p class="line red" style="top:714px">LED導入による管球</p>
  <p class="line red" style="top:765px">交換コストも削減</p>
  <div class="badge-circle small" style="left:70px;top:700px">更に</div>
  <div class="cost-tag" style="left:718px;top:740px"><small>COST DOWN</small><b>低</b></div>

  <p class="note">蛍光灯の寿命を10,000時間、LEDの寿命を40,000時間とした場合、交換費用は約4分の1。<br>白熱灯の寿命は約1,000時間のため、LEDの場合は交換回数が約40分の1になり、<br>交換費用や手間も大きく削減できます。</p>

  <p class="about">ミナセ電力の関連団体は、中央エネルギー機構・グリーン環境協会・エコライフ東京・省エネ推進協議会各機関の<strong>無料省エネ診断の診断事業者</strong>です。<em>数多くの診断の実績がある新電力会社</em>だからこそ、お客様の立場で考え最もお客様が喜ぶ提案をする事ができるのです。</p>

  <div class="brand"><i></i><span>ミナセ電力</span></div>
  <p class="brand-sub">Minase Power</p>
</main>
</body>
</html>
```